High Quality fast food restaurant - Tomanyo

Tomanyo is a fast food company with its target's focused on logistic, simplicity, high quality, freshness and modern.

We need a web design where the customers can get a complete idea of our high quality completeness, we want to take fast food to a new upper level.

We would like to see the colours of wood and metal. Pictures have been attached of our local.

We would like to have something in similar to: http://www.qpz.example/
Updates

Images for the food we are going to sell can be found here: http://shrt.example/uWQa7

It will be the images with rice, french fries or pita bread.

Target Market(s)

The fast food eating people between sloppy food and restaurant level.

Industry/Entity Type

Fast Food Restaurant

Requirements
Should not have
• No Flash or Java

```html
<!DOCTYPE html>
<html lang="en">
<head>
<meta charset="utf-8">
<title>Tomanyo – Fast Food</title>
<link rel="stylesheet" href="https://fonts.googleapis.com/css2?family=Roboto+Condensed:wght@400;700&family=PT+Sans:wght@400;700&display=swap">
<style>
:root{
  --wood-dark:#2e221c;
  --wood-mid:#4a372d;
  --brand-red:#c0250f;
  --nav-active:#ef4a23;
  --text-grey:#555;
  --text-light:#fff;
  --band-grey:#e4e4e4;
  --caption-red:rgba(214,58,52,.9);
  --caption-grey:rgba(70,70,70,.85);
  --signup:#f2a413;
}
*{margin:0;padding:0;box-sizing:border-box}
html,body{width:1200px;height:995px;overflow:hidden;background:#fff}
body{position:relative;font-family:"PT Sans",sans-serif}
.wood{background:linear-gradient(90deg,var(--wood-dark),var(--wood-mid) 30%,#3a2a22 55%,var(--wood-mid) 80%,var(--wood-dark))}
.site-header{position:absolute;left:0;top:0;width:1200px;height:64px}
.brand{position:absolute;left:189px;top:6px;font-family:"Roboto Condensed",sans-serif;font-weight:700;font-size:46px;line-height:50px;color:var(--text-light);letter-spacing:1.5px}
.divider{position:absolute;top:0;width:1px;height:64px;background:rgba(0,0,0,.45)}
.main-nav a{position:absolute;top:21px;font-family:"Roboto Condensed",sans-serif;font-size:17.5px;line-height:22px;color:var(--text-light);text-decoration:none;white-space:nowrap}
.main-nav a.active{color:var(--nav-active)}
.hero{position:absolute;left:0;top:64px;width:1200px;height:450px;overflow:hidden}
.hero-photo{position:absolute;inset:0;background:radial-gradient(circle at 820px 330px,#e7a34f 0,#d88b3a 90px,transparent 230px),radial-gradient(circle at 430px 260px,#f3ece6 0,#e6dbd2 220px,transparent 360px),linear-gradient(90deg,#c9b7a6,#e8ddd2 40%,#d8a06a 75%,#c98e4c)}
.hero-arrow{position:absolute;top:196px}
.caption-title{position:absolute;left:180px;top:274px;width:339px;height:37px;background:var(--caption-red);color:var(--text-light);font-family:"Roboto Condensed",sans-serif;font-size:21.5px;line-height:37px;padding-left:18px;white-space:nowrap}
.caption-sub{position:absolute;left:180px;top:317px;width:451px;height:37px;background:var(--caption-grey);color:var(--text-light);font-family:"Roboto Condensed",sans-serif;font-size:13.5px;line-height:37px;padding-left:17px;white-space:nowrap;overflow:hidden;letter-spacing:-.1px}
.welcome{position:absolute;left:0;top:514px;width:1200px;height:109px;background:var(--band-grey);text-align:center}
.welcome h1{margin-top:18px;font-family:"Roboto Condensed",sans-serif;font-weight:400;font-size:32px;line-height:36px;color:var(--brand-red)}
.welcome p{width:830px;margin:9px auto 0;font-size:8.7px;line-height:15px;color:var(--text-grey);text-transform:uppercase}
.feature{position:absolute;top:644px;width:266px}
.feature h2{font-family:"Roboto Condensed",sans-serif;font-weight:400;font-size:19.5px;line-height:22px;color:#444;white-space:nowrap}
.feature h2 strong{display:block;font-size:26.5px;line-height:28px;color:var(--brand-red);font-weight:400}
.feature-media{position:absolute;top:57px;left:0;width:266px;height:142px}
.feature-cta{position:absolute;left:0;bottom:0;width:100%;height:31px;background:rgba(50,50,50,.75);color:var(--text-light);font-family:"Roboto Condensed",sans-serif;font-size:16px;line-height:31px;padding-left:11px;white-space:nowrap}
.feature p{position:absolute;top:208px;font-size:9px;line-height:15.4px;color:var(--text-grey)}
.events{position:absolute;left:752px;top:647px;width:268px}
.events-title{font-family:"Roboto Condensed",sans-serif;font-weight:400}
.events-title .lead{display:block;font-size:19.5px;line-height:22px;color:#444}
.events-title .main{display:block;font-size:28.5px;line-height:30px;color:var(--brand-red)}
.player{position:absolute;left:2px;top:54px;width:266px;height:168px;background:#111;border:2px solid #333}
.player-screen{position:absolute;left:3px;top:3px;right:3px;height:140px;background:linear-gradient(180deg,#2b2b2b,#3e3e3e 55%,#1e1e1e)}
.site-footer{position:absolute;left:0;top:913px;width:1200px;height:82px}
.footer-nav{position:absolute;left:182px;top:24px;font-size:8.5px;color:var(--text-light);text-transform:uppercase;font-weight:700;white-space:nowrap}
.footer-nav span{margin:0 15.5px}
.copyright{position:absolute;left:182px;top:42px;font-size:8px;color:var(--text-light)}
.newsletter h3{position:absolute;left:602px;top:13px;font-family:"Roboto Condensed",sans-serif;font-weight:400;font-size:20px;color:var(--text-light)}
.newsletter .field{position:absolute;left:599px;top:42px;width:197px;height:19px;background:#6b6460;border:1px solid #857c76;color:var(--text-light);font-size:7px;font-weight:700;line-height:17px;padding-left:8px}
.newsletter .btn{position:absolute;left:805px;top:42px;width:68px;height:19px;background:var(--signup);border:1px solid #c77f00;color:#3a2200;font-size:9px;font-weight:700;line-height:17px;text-align:center}
.social{position:absolute;left:936px;top:29px}
</style>
</head>
<body>

<header class="site-header wood">
  <div class="brand">TOMANYO</div>
  <span class="divider" style="left:411px"></span>
  <span class="divider" style="left:806px"></span>
  <span class="divider" style="left:1020px"></span>
  <nav class="main-nav">
    <a class="active" href="#" style="left:470px">HOME</a>
    <a href="#" style="left:537px">ABOUT US</a>
    <a href="#" style="left:634px">PRODUCTS</a>
    <a href="#" style="left:727px">SERVICES</a>
    <a href="#" style="left:824px">SPECIALS</a>
    <a href="#" style="left:921px">CONTACT US</a>
  </nav>
</header>

<section class="hero">
  <div class="hero-photo" role="img" aria-label="Fruit yogurt cups beside a crispy chicken burger with cheese and lettuce"></div>
  <svg class="hero-arrow" style="left:180px" width="34" height="34" viewBox="0 0 34 34"><circle cx="17" cy="17" r="15.5" fill="none" stroke="#fff" stroke-opacity=".7" stroke-width="2"/><path d="M20 9 L11 17 L20 25" fill="none" stroke="#fff" stroke-opacity=".8" stroke-width="2.5"/></svg>
  <svg class="hero-arrow" style="left:984px" width="34" height="34" viewBox="0 0 34 34"><circle cx="17" cy="17" r="15.5" fill="none" stroke="#fff" stroke-opacity=".7" stroke-width="2"/><path d="M14 9 L23 17 L14 25" fill="none" stroke="#fff" stroke-opacity=".8" stroke-width="2.5"/></svg>
  <div class="caption-title">LOREM IPSUM IS SIMPLY DUMMY</div>
  <div class="caption-sub">LOREM IPSUM IS SIMPLY DUMMY TEXT OF THE PRINTING AND TYPESETTING</div>
</section>

<section class="welcome">
  <h1>WELCOME TO TOMANYO</h1>
  <p>Lorem Ipsum is simply dummy text of the printing and typesetting industry. Lorem Ipsum has been the industry's standard dummy text ever since the 1500s, when an unknown printer took a galley of type and scrambled it to make a type specimen book. It has survived not only five centuries, but also the leap into electronic typesetting.</p>
</section>

<article class="feature" style="left:180px">
  <h2>VIEW ALL OFFERS <strong>AND PROMOTIONS</strong></h2>
  <div class="feature-media">
    <div role="img" aria-label="Grilled chicken slices with roast potatoes and salad" style="position:absolute;inset:0;background:linear-gradient(135deg,#7a3a12,#d98a3a 45%,#e9c45a 70%,#8a4a1e)"></div>
    <div class="feature-cta">CLICK HERE TO VIEW MORE</div>
  </div>
  <p>Lorem Ipsum is simply dummy text of the printing and typesetting industry. Lorem Ipsum has been the industry's standard dummy text ever since the 1500s.</p>
</article>

<article class="feature" style="left:468px">
  <h2>VIEW ALL PRODUCTS <strong>AND SPECIAL</strong></h2>
  <div class="feature-media">
    <div role="img" aria-label="Baguette sandwich with egg slices and herbs on paper" style="position:absolute;inset:0;background:linear-gradient(150deg,#e8e3dc,#c98a4a 45%,#b86e30 60%,#ddd6cc)"></div>
    <div class="feature-cta">CLICK HERE TO VIEW MORE</div>
  </div>
  <p>Lorem Ipsum is simply dummy text of the printing and typesetting industry. Lorem Ipsum has been the industry's standard dummy text ever since the 1500s.</p>
</article>

<article class="events">
  <h2 class="events-title"><span class="lead">VIEW ALL</span><span class="main">EVENTS</span></h2>
  <div class="player">
    <div class="player-screen" role="img" aria-label="Video still of the restaurant interior and counter"></div>
    <svg style="position:absolute;left:0;top:0" width="262" height="164" viewBox="0 0 262 164">
      <circle cx="131" cy="73" r="27" fill="#777" stroke="#999" stroke-width="2"/>
      <path d="M120 65 L142 65 L131 84 Z" fill="#444"/>
      <rect x="0" y="144" width="262" height="20" fill="#1a1a1a"/>
      <rect x="9" y="149" width="3" height="10" fill="#aaa"/><rect x="15" y="149" width="3" height="10" fill="#aaa"/>
      <path d="M34 152 h3 l4 -3 v10 l-4 -3 h-3 z" fill="#aaa"/>
      <rect x="44" y="153" width="2" height="6" fill="#777"/><rect x="48" y="151" width="2" height="8" fill="#777"/>
      <text x="60" y="158" fill="#ddd" font-family="PT Sans,sans-serif" font-size="9">0:04 / 0:30</text>
      <rect x="112" y="151" width="112" height="6" fill="#333"/>
      <rect x="112" y="151" width="12" height="6" fill="#d22"/>
      <rect x="124" y="151" width="36" height="6" fill="#666"/>
      <circle cx="124" cy="154" r="5" fill="#ccc"/>
      <path d="M241 149 l-3 0 0 3 M251 149 l3 0 0 3 M241 159 l-3 0 0 -3 M251 159 l3 0 0 -3" stroke="#999" fill="none"/>
    </svg>
  </div>
</article>

<footer class="site-footer wood">
  <div class="footer-nav">Home<span>|</span>About us<span>|</span>Products<span>|</span>Services<span>|</span>Specials<span>|</span>Contact us</div>
  <div class="copyright">© 2013 TOMANYO. ALL RIGHTS RESERVED</div>
  <div class="newsletter">
    <h3>NEWSLETTER</h3>
    <div class="field">ENTER YOUR SIGNUP :</div>
    <div class="btn">SIGNUP</div>
  </div>
  <svg class="social" width="90" height="24" viewBox="0 0 90 24" aria-label="Social links">
    <circle cx="11" cy="11" r="11" fill="#2b5ca8"/>
    <circle cx="41" cy="11" r="11" fill="#3fb1e3"/>
    <circle cx="70" cy="11" r="11" fill="#ee7b1e"/>
  </svg>
</footer>

</body>
</html>
```